Now Hiring Drivers or Help Wanted Ad

I am looking for an ad to be used for digital marketing for employment. Below is some or all of the information to work into the ad.

KORVA Holdings, LLC is a stable and premier hauler operating in the Northeast Wisconsin region since 1994. We have a variety of equipment from Dump Trucks, Roll Off Trucks to Semis with Belt Trailers, Walking Floors, Gondolas, Tankers, Vans and Compacting Trailers offering a variety of positions with different routes to mix up your day or settle into something you enjoy. We also offer low boy services and some flat bed work. We haul various materials from general aggregate freight to various types of non-hazardous wastes such as garbage, recyclables, paper mill sludge, metal, shredder fluff to various landfills or recycling centers.

Rate of pay is based on experience and the variety of equipment you are able to operate or your willingness to learn.

All work is local and you are home every night.

Great Pay
Sign on Bonus
Holiday & Vacation Pay
Health Insurance, Vision & Dental Offered
Employer Paid Life Insurance
Uniforms
Phone Reimbursement
PLUMEX

Industry/Entity Type

Trucking and Excavation

Colors
EB3D1F
EC4F4E
F09395
F8D3D4
FCEDEE

Requirements
Must have
• Should have some of the same look/feel of the ad attached.

```html
<!DOCTYPE html>
<html lang="en">
<head>
<meta charset="utf-8">
<title>KORVA Holdings – Now Hiring Drivers</title>
<link href="https://fonts.googleapis.com/css2?family=Montserrat:wght@500;700;900&family=Barlow+Condensed:wght@600&display=swap" rel="stylesheet">
<style>
  :root{
    --stage:#404040;
    --red:#eb2f25;
    --red-deep:#8e1014;
    --yellow:#fde93a;
    --ink:#2a2a2e;
    --white:#f1f1f1;
    --green-a:#5fae6a;
    --green-b:#8fc79a;
    --gravel:#b9b3a6;
  }
  *{margin:0;padding:0;box-sizing:border-box}
  html,body{width:1200px;height:1200px;overflow:hidden;background:var(--stage)}
  .poster{position:absolute;left:205px;top:88px;width:791px;height:1024px;overflow:hidden;font-family:"Montserrat",sans-serif}
  .site-photo{position:absolute;left:0;top:0;width:791px;height:480px;
    background:linear-gradient(160deg,var(--green-a) 0%,var(--green-b) 45%,var(--gravel) 100%)}
  .shapes{position:absolute;left:0;top:0}
  .headline{position:absolute;top:104px;left:93px;white-space:nowrap;font-weight:900;line-height:1}
  .headline .now{font-size:70px;color:var(--ink);letter-spacing:-1px}
  .headline .hiring{font-size:96px;color:var(--red);margin-left:20px;letter-spacing:1px}
  .ribbon-text{position:absolute;left:121px;width:542px;top:212px;text-align:center;font-weight:900;font-size:88px;color:var(--white);line-height:1;letter-spacing:1px}
  .truck-photo{position:absolute;left:0;top:560px;width:503px;height:404px;
    background:linear-gradient(120deg,#b9b9b9 0%,#c9252a 45%,#a8161b 100%);opacity:.9}
  .brand{position:absolute;left:134px;top:480px;width:240px;text-align:center;color:#4fb65a;font-weight:900;font-size:30px;line-height:1.05}
  .brand small{display:block;font-size:10px;font-weight:900;margin-top:4px}
  .lead{position:absolute;left:386px;top:488px;width:380px;color:var(--yellow);font-weight:700;font-size:23px;line-height:1.35}
  .note{position:absolute;left:386px;top:558px;width:380px;color:#fff;font-weight:500;font-size:13.5px;line-height:1.5}
  .perks{position:absolute;list-style:none;font-family:"Barlow Condensed",sans-serif;font-weight:600;font-size:22px;color:#fff;line-height:1.1}
  .perks li{position:absolute;white-space:nowrap;display:flex;align-items:flex-start;gap:10px}
  .perks svg{flex:none;margin-top:4px}
  .footer{position:absolute;left:0;top:964px;width:791px;height:60px;background:var(--yellow);display:flex;align-items:center;justify-content:center;gap:14px;color:var(--red);font-weight:700;font-size:27px}
  .footer .divider{width:2px;height:32px;background:var(--red)}
  .footer span{display:flex;align-items:center;gap:8px}
</style>
</head>
<body>
<div class="poster">
  <div class="site-photo" role="img" aria-label="Aerial view of the company yard with buildings, trucks and material piles, green tinted"></div>

  <svg class="shapes" width="791" height="1024" viewBox="0 0 791 1024">
    <defs>
      <linearGradient id="redFade" x1="0" y1="0" x2="0" y2="1">
        <stop offset="0" stop-color="#f22d24"/>
        <stop offset=".55" stop-color="#e0262a"/>
        <stop offset="1" stop-color="#8e1014"/>
      </linearGradient>
    </defs>
    <path d="M0 457 C120 396 230 366 320 368 C440 371 520 446 620 448 C700 450 760 426 791 406 L791 1024 L0 1024 Z" fill="var(--yellow)"/>
    <path d="M0 482 C120 420 230 384 320 386 C440 389 520 466 620 468 C700 470 760 446 791 428 L791 1024 L0 1024 Z" fill="url(#redFade)"/>
    <path d="M121 206 L663 206 L640 252 L663 299 L121 299 L144 252 Z" fill="var(--red)"/>
  </svg>

  <div class="headline"><span class="now">NOW</span><span class="hiring">HIRING</span></div>
  <div class="ribbon-text">DRIVERS</div>

  <div class="truck-photo" role="img" aria-label="Red dump truck cab with a driver in a hi-vis shirt standing beside it"></div>

  <div class="brand">KORVA Holdings, LLC<small>LAKEVIEW, WI</small></div>

  <p class="lead">All work is local and you are home every night.</p>
  <p class="note">Rate of pay is based on experience and the variety of equipment you are able to operate or your willingness to learn.</p>

  <ul class="perks">
    <li style="left:386px;top:650px"><svg width="16" height="14" viewBox="0 0 16 14"><path d="M1 7 L6 12 L15 1" fill="none" stroke="var(--yellow)" stroke-width="3"/></svg>Great Pay</li>
    <li style="left:512px;top:650px"><svg width="16" height="14" viewBox="0 0 16 14"><path d="M1 7 L6 12 L15 1" fill="none" stroke="var(--yellow)" stroke-width="3"/></svg>Sign on Bonus</li>
    <li style="left:664px;top:651px"><svg width="16" height="14" viewBox="0 0 16 14"><path d="M1 7 L6 12 L15 1" fill="none" stroke="var(--yellow)" stroke-width="3"/></svg>Uniforms</li>
    <li style="left:512px;top:692px"><svg width="16" height="14" viewBox="0 0 16 14"><path d="M1 7 L6 12 L15 1" fill="none" stroke="var(--yellow)" stroke-width="3"/></svg>Holiday &amp; Vacation Pay</li>
    <li style="left:512px;top:736px"><svg width="16" height="14" viewBox="0 0 16 14"><path d="M1 7 L6 12 L15 1" fill="none" stroke="var(--yellow)" stroke-width="3"/></svg>Health Insurance, Vision<br>&amp; Dental Offered</li>
    <li style="left:512px;top:806px"><svg width="16" height="14" viewBox="0 0 16 14"><path d="M1 7 L6 12 L15 1" fill="none" stroke="var(--yellow)" stroke-width="3"/></svg>Employer Paid Life Insurance</li>
    <li style="left:512px;top:850px"><svg width="16" height="14" viewBox="0 0 16 14"><path d="M1 7 L6 12 L15 1" fill="none" stroke="var(--yellow)" stroke-width="3"/></svg>Phone Reimbursement</li>
    <li style="left:512px;top:889px"><svg width="16" height="14" viewBox="0 0 16 14"><path d="M1 7 L6 12 L15 1" fill="none" stroke="var(--yellow)" stroke-width="3"/></svg>PLUMEX</li>
  </ul>

  <div class="footer">
    <span><svg width="18" height="18" viewBox="0 0 20 20"><circle cx="10" cy="10" r="8" fill="none" stroke="var(--red)" stroke-width="2"/><ellipse cx="10" cy="10" rx="3.5" ry="8" fill="none" stroke="var(--red)" stroke-width="1.6"/><path d="M2 10 H18" stroke="var(--red)" stroke-width="1.6"/></svg>www.korvaholdingsllc.com</span>
    <div class="divider"></div>
    <span><svg width="18" height="18" viewBox="0 0 20 20"><path d="M5 2 L8 6 L6 8 C7 11 9 13 12 14 L14 12 L18 15 L16 18 C9 17 3 11 2 4 Z" fill="none" stroke="var(--red)" stroke-width="2" stroke-linejoin="round"/></svg>920-555-0147</span>
  </div>
</div>
</body>
</html>
```